Outdoor sign for Brindle Auto Restoration

I need a horizontal 4'x 8' outdoor roadside sign for my classic auto restoration business. I have uploaded colors and our logo. Needs the Brindle name, a prominent Classic AUTO RESTORATION, phone number and website. We rebuild and restore vintage cars, trucks and 4x4s. I'd like something clean but possibly retro. Classic Auto Restoration is more important than the Brindle name. It needs to be visible and readable from the street. NO CLIP ART

Target Market(s)

Customers who need their vintage care restored or upgraded. Men and women ages 25-75

Industry/Entity Type

Automotive

Colors
FFC000
F8CF3A
FAE287
FDF2CF
FEFAEE

Requirements
Must have
• Legible. Bright. Readable as a backlit 4' x 8' large horizontal sign (roughly 120cm X 240cm)
Nice to have
• Use of the Brindle logo/type, Complete or Classic before prominent AUTO RESTORATION
Should not have
• Clip art of old cars or icons. And we don't want the Brindle Logo from the website because it wont be legible from the road. I have included the Illustrator file for Brindle text in the uploads

```html
<!DOCTYPE html>
<html lang="en">
<head>
<meta charset="utf-8">
<title>Brindle Auto Restoration – Roadside Sign</title>
<link rel="stylesheet" href="https://fonts.googleapis.com/css2?family=Anton&family=Great+Vibes&family=Roboto+Condensed:wght@500;700&display=swap">
<style>
  :root {
    --sign-black: #231f20;
    --sign-gold: #f7ae1a;
    --sign-white: #ffffff;
  }
  html, body {
    margin: 0;
    padding: 0;
    width: 1200px;
    height: 600px;
    overflow: hidden;
    background: var(--sign-black);
  }
  .sign {
    display: block;
    width: 1200px;
    height: 600px;
  }
  .sign__background { fill: var(--sign-black); }
  .sign__rule { fill: var(--sign-gold); }
  .sign__script {
    font-family: "Great Vibes", cursive;
    font-size: 150px;
    fill: var(--sign-gold);
  }
  .sign__headline {
    font-family: "Anton", sans-serif;
    font-size: 232px;
    fill: var(--sign-white);
  }
  .sign__phone {
    font-family: "Roboto Condensed", sans-serif;
    font-weight: 700;
    font-size: 70px;
    fill: var(--sign-white);
  }
  .sign__brand {
    font-family: "Anton", sans-serif;
    font-size: 97px;
    fill: var(--sign-gold);
  }
  .sign__web {
    font-family: "Roboto Condensed", sans-serif;
    font-weight: 500;
    font-size: 46px;
    fill: var(--sign-white);
  }
</style>
</head>
<body>
<svg class="sign" viewBox="0 0 1200 600" xmlns="http://www.w3.org/2000/svg" role="img" aria-label="Classic Auto Restoration – Brindle – 555-014-2290 – brindleautoworks.com">
  <rect class="sign__background" x="0" y="0" width="1200" height="600"/>

  <text class="sign__script" x="600" y="132" text-anchor="middle">Classic</text>

  <rect class="sign__rule" x="0" y="195" width="1200" height="5.5"/>
  <text class="sign__headline" x="34" y="381" textLength="1125" lengthAdjust="spacingAndGlyphs">AUTO RESTORATION</text>
  <rect class="sign__rule" x="0" y="400" width="1200" height="5.5"/>

  <text class="sign__phone" x="37" y="546" textLength="301" lengthAdjust="spacingAndGlyphs">555-014-2290</text>
  <text class="sign__brand" x="393" y="555" textLength="415" lengthAdjust="spacingAndGlyphs">BRINDLE</text>
  <text class="sign__web" x="862" y="533" textLength="302" lengthAdjust="spacingAndGlyphs">brindleautoworks.com</text>
</svg>
</body>
</html>
```